Modellprojekt in der Jugendhilfe sucht für Abschlussbroschüre ansprechendes Design
Zielgruppe
Wir sind ein Jugendhilfeträger und haben kürzlich ein dreijähriges Modellprojekt 'Qualitätsmarke-Gemeinsame Familienbegleitung' (Signet 'QM_Anerkennung' liegt anbei) beendet. Zielgruppen sind zum Einen Kinder und Jugendliche, die in Erziehungshilfe-Wohngruppen leben und zum Anderen Fach- und Führungskräfte in der Kinder- und Jugendhilfe. Über Ablauf und Schlussfolgerungen aus dem abgeschlossenen Modellprojekt soll eine 30-seitige Broschüre mit dem Titel 'Hier wächst Mitsprache' Untertitel 'Ein Wegweiser zur Qualitätsmarke' Auskunft geben.
Aufgabenstellung
- Broschüre im DIN A4 - Format,
- Dummy-Text für Projektstruktur und -beteiligte,
- Formschönes und dynamisches Design,
- Platzhalter für eigene Bilder (max. 3 pro Seite),
- die 6 Einrichtungslogos in einer Reihe auf dem Deckblatt vorne (unten),
- Der Broschüreninhalt ist in der PDF 'Kurzvorstellung enthalten',
- Vorgaben zum CD im PDF 'Hauptmanual KWF',
- Das KWF-Signet, wie im Manual beschrieben,
- das ebenfalls hochgeladene Gütesiegel kommt auf das Deckblatt

```html
<!DOCTYPE html>
<html lang="de">
<head>
<meta charset="utf-8">
<title>Hier wächst Mitsprache – Broschüre Deckblatt</title>
<link rel="stylesheet" href="https://fonts.googleapis.com/css2?family=Source+Sans+3:wght@400;600&display=swap">
<style>
  :root {
    --stage: #d9dadc;
    --paper: #e9ecf1;
    --strip: #f7f8fa;
    --ink: #4a4a4a;
    --ink-soft: #6b6b6b;
    --brand-blue: #3f8bcc;
    --line-dark: #2f5d8f;
    --line-light: #6fa3d6;
    --seal-green: #3d9a86;
    --seal-ring: #6cc45a;
    --sketch-blue: #a9c2e4;
    --sketch-grey: #d3d8e0;
    --accent-orange: #e98a3c;
  }
  * { box-sizing: border-box; margin: 0; padding: 0; }
  html, body { width: 1200px; height: 1000px; overflow: hidden; }
  body {
    background: var(--stage);
    font-family: "Source Sans 3", "Segoe UI", sans-serif;
    display: flex;
    align-items: center;
    justify-content: center;
  }
  .cover {
    position: relative;
    width: 664px;
    height: 940px;
    background: var(--paper);
    box-shadow: 0 10px 30px rgba(0,0,0,.18);
    overflow: hidden;
  }
  .partner-row {
    position: absolute;
    top: 40px;
    left: 130px;
    right: 24px;
    display: flex;
    background: var(--strip);
  }
  .partner {
    flex: 1;
    display: flex;
    align-items: center;
    gap: 5px;
    padding: 12px 6px;
    font-size: 9.5px;
    line-height: 1.15;
    color: var(--ink);
  }
  .partner-mark {
    flex: none;
    width: 11px;
    height: 11px;
    border-radius: 50%;
    background: var(--accent-orange);
  }
  .partner:nth-child(3) .partner-mark { background: var(--brand-blue); }
  .seal {
    position: absolute;
    top: 118px;
    left: 240px;
    width: 124px;
    height: 124px;
  }
  .artwork {
    position: absolute;
    border-radius: 10px;
    background: linear-gradient(135deg, var(--sketch-grey), var(--sketch-blue));
  }
  .artwork--boy { top: 300px; left: 170px; width: 160px; height: 210px; }
  .artwork--girl { top: 250px; left: 410px; width: 160px; height: 160px; }
  .swoosh {
    position: absolute;
    inset: 0;
    width: 664px;
    height: 940px;
  }
  .sponsor {
    position: absolute;
    right: 40px;
    top: 600px;
    display: flex;
    align-items: flex-start;
    gap: 10px;
    padding: 8px;
    background: var(--strip);
    width: 220px;
  }
  .sponsor-mark {
    flex: none;
    width: 60px;
    height: 60px;
    background: var(--brand-blue);
  }
  .sponsor-name {
    font-size: 12.5px;
    line-height: 1.2;
    color: var(--ink-soft);
  }
  .title-block {
    position: absolute;
    left: 60px;
    right: 60px;
    top: 770px;
    text-align: right;
  }
  .title {
    font-size: 46px;
    font-weight: 400;
    line-height: 1.1;
    color: var(--ink);
  }
  .subtitle {
    display: inline-block;
    margin-top: 8px;
    padding: 3px 12px;
    background: var(--brand-blue);
    color: #fff;
    font-size: 23px;
    font-weight: 400;
  }
</style>
</head>
<body>
  <main class="cover">
    <div class="partner-row">
      <div class="partner"><span class="partner-mark"></span>Verbund Lindenhof</div>
      <div class="partner"><span class="partner-mark"></span>Jugendwerk Am Deich</div>
      <div class="partner"><span class="partner-mark"></span>Kinderhäuser Birkenweg</div>
      <div class="partner"><span class="partner-mark"></span>Jugendhilfe Heideland</div>
      <div class="partner"><span class="partner-mark"></span>Hilfen Am Moorbach</div>
    </div>

    <svg class="seal" viewBox="0 0 124 124" role="img" aria-label="Qualitätssiegel des Projekts">
      <circle cx="62" cy="62" r="46" fill="var(--seal-green)" stroke="var(--seal-ring)" stroke-width="4"/>
    </svg>

    <div class="artwork artwork--boy" role="img" aria-label="Kinderzeichnung: springender Junge mit ausgebreiteten Armen"></div>
    <div class="artwork artwork--girl" role="img" aria-label="Kinderzeichnung: tanzendes Mädchen im Kleid"></div>

    <svg class="swoosh" viewBox="0 0 664 940" aria-hidden="true">
      <path d="M0 770 C 150 610, 350 590, 490 545 S 640 400, 664 300" fill="none" stroke="var(--line-dark)" stroke-width="2"/>
      <path d="M0 755 C 160 600, 360 575, 495 528 S 630 380, 650 270" fill="none" stroke="var(--line-light)" stroke-width="1.6"/>
    </svg>

    <div class="sponsor">
      <span class="sponsor-mark"></span>
      <span class="sponsor-name">Gruppe KWF<br>Kieler Werkverbund<br>für Familien</span>
    </div>

    <div class="title-block">
      <h1 class="title">Hier wächst Mitsprache</h1>
      <p class="subtitle">Ein Wegweiser zur Qualitätsmarke</p>
    </div>
  </main>
</body>
</html>
```